Brightivo sanitzing wipes: logo, inner foil 6*8cm and consumer carton

we need a clever but simple logo design for a product and integrated look for the packaging (inner foil 6*8 cm and consumer carton). texts are provided for each and some examples of other products and formatting. we would use very simple imagery and color schemes. the main theme is safety, convenience, utility.

for the winning design we will for sure have some changes and adaptations and i would pay additionally for those.

Target Market(s)

American and European retail mass merchants -- wholesale stores, online, retail

Industry/Entity Type

Health And Wellness

Font styles to use
Sans Serif

Requirements
Must have
• Correct formatting of texts in accordance to regulations. Clear communication of texts in an easy to read and understandable formatting. Engaging, but simple design.
Nice to have
• Interesting use of color and contrast. some decent imagery/visual graphics that can make the outter packaging pop on shelf.
Should not have
• odd fonts or formatting. knock-offs of other designs of a similar product in its category, cliché or overused imagery

```html
<!DOCTYPE html>
<html lang="en">
<head>
<meta charset="UTF-8">
<title>Brightivo Sanitizing Hand Wipes – Foil Sachet</title>
<link rel="stylesheet" href="https://fonts.googleapis.com/css2?family=Montserrat:wght@300;400;600;700&display=swap">
<style>
  :root {
    --backdrop: #c7bba2;
    --foil-deep: #1487c4;
    --foil-mid: #2aa6dd;
    --foil-light: #6fdcf6;
    --ink-strong: #e6ecef;
    --ink-soft: #d3dde2;
  }
  * { margin: 0; padding: 0; box-sizing: border-box; }
  html, body {
    width: 1200px; height: 960px; overflow: hidden;
    background: var(--backdrop);
    font-family: "Montserrat", sans-serif;
  }
  .sachet {
    position: absolute; left: 345px; top: 124px; width: 528px; height: 726px;
    background: linear-gradient(120deg, var(--foil-deep) 0%, var(--foil-mid) 45%, var(--foil-light) 78%, var(--foil-mid) 100%);
    border-radius: 3px;
  }
  .seal { position: absolute; inset: 0; }
  .content { position: absolute; inset: 0; color: var(--ink-strong); }
  .line { position: absolute; left: 64px; width: 394px; white-space: nowrap; }

  .brand {
    position: absolute; left: 0; width: 100%; top: 92px; height: 64px;
    display: flex; justify-content: center; align-items: center; gap: 12px;
  }
  .brand-dot { width: 16px; height: 16px; border-radius: 50%; background: var(--ink-strong); }
  .brand-name { font-weight: 300; font-size: 58px; line-height: 64px; color: var(--ink-strong); }

  .product-title { position: absolute; left: 0; width: 100%; text-align: center; font-size: 21.5px; line-height: 24px; }
  .product-title.strong { top: 164px; font-weight: 700; }
  .product-title.light { top: 187px; font-weight: 400; }

  .facts-heading { top: 256px; font-size: 33px; line-height: 44px; font-weight: 700; }
  .rule { position: absolute; left: 64px; width: 394px; background: var(--ink-strong); }
  .rule.heavy { top: 308px; height: 5px; }
  .rule.thin { top: 338px; height: 1.5px; }
  .rule.mid { top: 365px; height: 2.5px; }

  .fact-row { display: flex; justify-content: space-between; font-size: 14px; line-height: 20px; }
  .fact-row.head { top: 317px; font-weight: 700; }
  .fact-row.body { top: 342px; font-weight: 400; font-size: 14.5px; color: var(--ink-soft); }

  .section-label { font-size: 14px; line-height: 20px; font-weight: 700; color: var(--ink-soft); }
  .label-use { top: 381px; }
  .label-warn { top: 429px; }
  .label-dir { top: 588px; }
  .section-text { font-size: 14px; line-height: 20px; font-weight: 400; color: var(--ink-soft); }
  .use-item { top: 399px; }
  .use-item::before { content: "● "; font-size: 9px; vertical-align: 2px; }
  .dir-text { top: 607px; }

  .warnings-text { top: 453px; font-size: 14px; line-height: 16.9px; font-weight: 400; color: var(--ink-soft); white-space: normal; }
  .warnings-text span { display: block; text-align: justify; text-align-last: justify; white-space: nowrap; }
  .warnings-text span.last { text-align-last: left; }
</style>
</head>
<body>
  <div class="sachet">
    <svg class="seal" width="528" height="726" viewBox="0 0 528 726">
      <g stroke="rgba(255,255,255,0.28)" stroke-width="1.5" fill="none">
        <line x1="4" y1="8" x2="524" y2="8"/><line x1="4" y1="16" x2="524" y2="16"/>
        <line x1="4" y1="24" x2="524" y2="24"/><line x1="4" y1="32" x2="524" y2="32"/>
        <line x1="4" y1="696" x2="524" y2="696"/><line x1="4" y1="704" x2="524" y2="704"/>
        <line x1="4" y1="712" x2="524" y2="712"/><line x1="4" y1="720" x2="524" y2="720"/>
        <line x1="10" y1="36" x2="10" y2="692"/><line x1="18" y1="36" x2="18" y2="692"/>
        <line x1="26" y1="36" x2="26" y2="692"/><line x1="34" y1="36" x2="34" y2="692"/>
        <line x1="494" y1="36" x2="494" y2="692"/><line x1="502" y1="36" x2="502" y2="692"/>
        <line x1="510" y1="36" x2="510" y2="692"/><line x1="518" y1="36" x2="518" y2="692"/>
      </g>
      <rect x="42" y="42" width="444" height="642" rx="10" fill="none" stroke="rgba(255,255,255,0.15)" stroke-width="1.5"/>
      <path d="M528 85 L520 87 L520 92 L528 94 Z" fill="var(--backdrop)"/>
    </svg>
    <div class="content">
      <div class="brand">
        <span class="brand-dot"></span>
        <span class="brand-name">Brightivo</span>
      </div>
      <div class="product-title strong">SANITIZING HAND</div>
      <div class="product-title light">WIPES</div>

      <h2 class="line facts-heading">Drug facts</h2>
      <div class="rule heavy"></div>
      <div class="line fact-row head"><span>Active Ingredient</span><span>Purpose</span></div>
      <div class="rule thin"></div>
      <div class="line fact-row body"><span>Ethyl Alcohol 70%</span><span>Antimicrobial</span></div>
      <div class="rule mid"></div>

      <h3 class="line section-label label-use">Use</h3>
      <p class="line section-text use-item">Hand sanitizer</p>

      <h3 class="line section-label label-warn">Warnings:</h3>
      <p class="line warnings-text">
        <span>flammable, keep away from fire or flame. for external</span>
        <span>use only, do not use on eyes or if you are allergic to any</span>
        <span>ingredients. If eye contact occurs, rinse thoroughly</span>
        <span>with water. keep away from children, stop use and ask</span>
        <span>a doctor should irritation or redness appear and persist</span>
        <span>for 72 hours. If swallowed, seek medical help or call the</span>
        <span class="last">Poison Control center right away.</span>
      </p>

      <h3 class="line section-label label-dir">Directions:</h3>
      <p class="line section-text dir-text">Wipe Hands, Discard (Do Not Flush).</p>
    </div>
  </div>
</body>
</html>
```